Corlow Baptist Church signage beginning in parking lot and carrying through facility.

We want to design a theme/scheme for our signage. Parking lot banners that go on the light poles, banners in the foyer that promote classes being offered, a display about current missional projects- I want them to all have a common look. We have a blue and grey decor that it would need to fit with. The website is Corlow.org I have attached our logo that we use and like and would incorporate. We have six classes that we want to deisgn banners for. We want the banners simple with an icon representing each class- it is a 6 step process so each step would have a banner and icon that represents that step.

The included Word Doc has the description of the classes we want the banners to promote and then file with the banners were some that were presented but not the style I am after. I want simple and informative.
Updates

Project Deadline Extended
Reason: I have not had time to work with the designers contributing so I wanted to extend for five days. Thank you all for your amazing contributions.

Target Market(s)

People that come into our church and parking lot each week.

Industry/Entity Type

Church

Font styles to use
Serif

Colors
0255a3
3b7bb7
85acd3
eaf1f7
fbee3d
fbed22

Requirements
Must have
• Visually inviting, consistent look. A style that can be added to and expanded to include all of our print and signage. We are looking to have banners added to our light poles in our parking lots and want to have something like "welcome home" on those banners. Then we want to have a similar theme carried into our foyer to incorporate into the banners that we use to promote classes etc. and keep our members and visited engaged. We are also building a display of our current mission projects and opportunities and we want to have a consistent look for that as well.
• The idea of using simple Icons to represent the different classes on the banners is appealing to me. A simple background, simple font, simple borders, few colors, with a prominent Icon as the central focus.
Nice to have
• Icon type logos for each of the six banners that represent the six steps in our class series.

```html
<!DOCTYPE html>
<html lang="en">
<head>
<meta charset="utf-8">
<title>Corlow Baptist Church – Step One Banner</title>
<link href="https://fonts.googleapis.com/css2?family=Source+Sans+3:wght@600;700&display=swap" rel="stylesheet">
<style>
  :root {
    --stage: #000000;
    --paper: #ffffff;
    --royal: #0a4fa3;
    --royal-light: #2a73bb;
    --sun: #f6ef3a;
    --ink: #15163a;
  }
  * { margin: 0; padding: 0; box-sizing: border-box; }
  html, body {
    width: 1200px; height: 817px; overflow: hidden;
    background: var(--stage);
    font-family: "Source Sans 3", "Myriad Pro", Arial, sans-serif;
  }
  .banner {
    position: absolute; left: 341px; top: 0;
    width: 524px; height: 817px;
    background: var(--paper);
    overflow: hidden;
  }
  .brand {
    position: absolute; left: 0; top: 0; width: 100%; height: 268px;
    display: flex; align-items: center; justify-content: center; gap: 14px;
  }
  .brand-dot {
    width: 34px; height: 34px; border-radius: 50%;
    background: var(--sun);
  }
  .brand-name {
    font-weight: 700; font-size: 74px; color: var(--ink); line-height: 1;
  }
  .step-bar {
    position: absolute; left: 0; top: 270px; width: 524px; height: 85px;
    background: var(--royal);
    border: 3px solid var(--sun);
    display: flex; align-items: center; justify-content: center;
    color: var(--sun); font-weight: 700; font-size: 38px; letter-spacing: 0.5px;
  }
  .field {
    position: absolute; left: 0; top: 355px; width: 524px; height: 462px;
    background: linear-gradient(160deg, var(--royal) 0%, #1460ac 50%, var(--royal) 100%);
  }
  .emblem {
    position: absolute; left: 491px; top: 369px; width: 222px; height: 222px;
    border-radius: 50%;
    background: var(--royal);
    border: 3px solid var(--sun);
  }
  .emblem-icon { position: absolute; left: 545px; top: 414px; }
  .title {
    position: absolute; left: 341px; width: 524px; top: 604px;
    text-align: center; color: var(--sun); font-weight: 700;
    font-size: 36px; line-height: 41px;
  }
  .verse {
    position: absolute; left: 341px; width: 524px; top: 697px;
    text-align: center; color: var(--sun); font-weight: 600;
    font-size: 16.4px; line-height: 22px;
  }
</style>
</head>
<body>
  <div class="banner">
    <div class="brand">
      <span class="brand-dot"></span>
      <span class="brand-name">Corlow</span>
    </div>
    <div class="step-bar">STEP ONE</div>
    <div class="field" role="img" aria-label="Decorative pattern of large overlapping leaves in lighter blue"></div>
  </div>

  <div class="emblem"></div>
  <svg class="emblem-icon" width="118" height="118" viewBox="0 0 118 118" aria-label="Church icon">
    <g fill="var(--sun)">
      <polygon points="59,0 84,34 84,40 117,60 117,66 112,66 112,118 6,118 6,66 1,66 1,60 34,40 34,34"/>
    </g>
    <g fill="var(--royal)">
      <polygon points="59,8 78,34 78,38 40,38 40,34"/>
      <circle cx="59" cy="50" r="10"/>
      <circle cx="59" cy="50" r="7" fill="var(--sun)"/>
      <path d="M51,118 V90 Q59,76 67,90 V118 Z"/>
      <path d="M22,118 V100 Q27,91 32,100 V118 Z"/>
      <path d="M86,118 V100 Q91,91 96,100 V118 Z"/>
      <rect x="6" y="62" width="106" height="4"/>
      <rect x="38" y="40" width="3" height="78"/>
      <rect x="77" y="40" width="3" height="78"/>
    </g>
  </svg>

  <h1 class="title">CORLOW<br>101</h1>
  <p class="verse">And let us consider how to stimulate one another to love and<br>good deeds, not forsaking our own assembling together, as<br>is the habit of some, but encouraging one another; and all<br>the more as you see the day drawing near.<br>Hebrews 10:24–25</p>
</body>
</html>
```